Single Page Production Company Site

Clean. Simple. Minimalist site with one page.

No portfolio, just some text to communicate a general overview of what the company does.

We work for a very select group of clients, creating strong brand personalities online. The site is specifically minimal and not communicating too much about what we do.. we have a variety of capabilities to work with clients and prefer to be broad with just a simple landing page as the point of contact for our brand.
Updates

Christmas holidays are coming up, maybe people need some time away from work with family and friends... We can keep working on this and I will provide feedback as quickly as possible, but I understand if designers have other commitments during the coming days. Thanks for your hard work!

Industry/Entity Type

Design Agency

Coding

Coded - Design and coding required

Number of Pages Required

1 page

Font styles to use
Sans Serif

Requirements
Must have
• Clean, bold text headlines.
Nice to have
• Unsure about any images used in the design, would like to see options with or without.

```html
<!DOCTYPE html>
<html lang="en">
<head>
<meta charset="utf-8">
<title>Cedar Lane Studio — concept. create. complete.</title>
<link rel="stylesheet" href="https://fonts.googleapis.com/css2?family=Kalam:wght@400;700&family=Source+Sans+3:wght@400;600;700&display=swap">
<style>
:root{
  --nav-blue:#1670bd;
  --hero-bg:#ffffff;
  --intro-bg:#8090cb;
  --team-bg:#b8b8b8;
  --goal-bg:#cbcbcb;
  --get-bg:#ebebeb;
  --contact-bg:#cccccc;
  --field:#a9a9a9;
  --footer-bg:#1b1b1b;
  --base-bg:#101010;
  --ink:#111111;
  --white:#ffffff;
  --yellow:#ecec3a;
  --royal:#1c1cae;
  --orange:#e08a1c;
  --gold:#e8c41c;
  --red:#e01f1f;
  --violet-text:#4b4bae;
  --muted:#8a8a8a;
  --head:"Kalam", cursive;
  --body:"Source Sans 3", sans-serif;
}
*{box-sizing:border-box;margin:0;padding:0}
html,body{width:1200px;height:3130px;overflow:hidden}
body{font-family:var(--body);color:var(--ink);position:relative;background:var(--hero-bg)}
section,header,footer{position:absolute;left:0;width:1200px;overflow:hidden}
.abs{position:absolute}
.headline{font-family:var(--head);font-weight:400;font-size:50px;line-height:1.1;letter-spacing:1px}
.copy{font-size:21px;line-height:1.08}

/* nav */
.site-nav{top:0;height:42px;background:var(--nav-blue)}
.site-nav ul{list-style:none;display:flex;gap:34px;position:absolute;left:312px;top:24px}
.site-nav a{color:var(--white);text-decoration:none;font-size:11px;letter-spacing:.3px}
.nav-email{right:24px;top:3px;color:var(--white);font-size:11px}

/* hero */
.hero{top:42px;height:516px;background:var(--hero-bg)}
.hero-title{font-family:var(--head);font-weight:700;font-size:70px;width:100%;text-align:center;top:198px;letter-spacing:1px}

/* intro */
.intro{top:558px;height:618px;background:var(--intro-bg)}
.design-title{left:40px;top:30px;color:var(--yellow)}
.design-copy{left:40px;top:97px;width:520px;color:var(--white)}
.art-title{left:538px;top:232px;color:var(--royal)}
.art-copy{left:538px;top:296px;width:600px;color:var(--white)}
.ideas-title{left:36px;top:437px;color:var(--ink)}
.ideas-copy{left:36px;top:502px;width:600px;color:var(--ink)}

/* team */
.team{top:1176px;height:558px;background:var(--team-bg)}
.team-title{left:515px;top:32px;color:var(--orange)}
.team-copy{left:515px;top:97px;width:630px;color:var(--gold);font-size:21px}
.team-copy strong{font-size:28px;font-weight:700}
.size-title{left:26px;top:218px;color:var(--red)}
.size-copy{left:26px;top:290px;width:640px;color:var(--white);font-size:23px;line-height:1.3}
.size-copy strong{font-size:29px;font-weight:700;line-height:1.1}

/* goal */
.goal{top:1734px;height:560px;background:var(--goal-bg)}
.goal-title{left:402px;top:26px;color:var(--orange)}
.goal-copy{left:402px;top:92px;width:760px}
.goal-copy strong{font-size:28px}
.who-title{left:28px;top:272px;font-size:52px}
.who-copy{left:28px;top:346px;width:850px}
.who-copy strong{font-size:28px}

/* get you */
.get-you{top:2294px;height:331px;background:var(--get-bg);text-align:center}
.get-title{width:100%;top:66px;font-size:48px;color:var(--ink)}
.get-copy{left:290px;width:620px;top:140px;color:var(--violet-text);font-size:11px;line-height:1.3}
.get-copy p{margin-bottom:12px}

/* contact */
.contact{top:2625px;height:233px;background:var(--contact-bg)}
.contact-email{left:88px;top:40px;font-size:16px}
.form-title{left:370px;top:12px;font-size:18px;font-weight:700}
.field{left:370px;width:240px;height:33px;background:var(--field);font-size:11px;font-weight:700;padding:7px 8px}
.field-name{top:38px}.field-email{top:98px}.field-phone{top:160px}
.field-message{left:710px;top:38px;width:325px;height:122px}
.send-btn{left:710px;top:170px;width:68px;height:22px;background:var(--field);border-radius:3px;font-size:11px;font-weight:700;text-align:center;line-height:22px}

/* footer */
.site-footer{top:2858px;height:190px;background:var(--footer-bg)}
.social{left:238px;top:34px;display:flex;gap:22px}
.social span{width:16px;height:16px;border-radius:50%;background:#5a5a5a;display:block}
.newsletter-label{left:664px;top:34px;color:var(--white);font-size:10px;font-weight:700}
.newsletter-input{left:792px;top:24px;width:166px;height:34px;border:1px solid #bbb;border-radius:17px;color:#ddd;font-size:10px;padding:10px 20px}
.newsletter-input::after{content:"";position:absolute;right:10px;top:11px;width:11px;height:11px;border-radius:50%;background:#ccc}
.footer-rule{left:243px;top:80px;width:715px;height:1px;background:#333}
.footer-links{left:487px;top:126px;display:grid;grid-template-columns:repeat(4,122px);row-gap:8px;list-style:none}
.footer-links a{color:#aaa;font-size:9px;text-decoration:none;text-transform:uppercase}

.base{top:3048px;height:82px;background:var(--base-bg);color:var(--muted);font-size:8px;text-transform:uppercase}
.shop{left:245px;top:18px}
.pay-note{left:540px;top:18px;color:#444}
.cards{left:765px;top:14px;display:flex;gap:8px}
.cards span{width:20px;height:12px;background:#666;border-radius:2px;display:block}
.copyright{left:245px;top:56px}
.base-links{right:240px;top:56px;display:flex;gap:36px}
</style>
</head>
<body>

<header class="site-nav">
  <nav>
    <ul>
      <li><a href="#">ABOUT US</a></li>
      <li><a href="#">WHO WE ARE</a></li>
      <li><a href="#">WHAT WE DO</a></li>
      <li><a href="#">PORTFOLIO</a></li>
      <li><a href="#">BLOG</a></li>
      <li><a href="#">CONTACT US</a></li>
      <li><a href="#">FAQ</a></li>
    </ul>
  </nav>
  <span class="abs nav-email">hello@cedarlanestudio.com</span>
</header>

<section class="hero">
  <h1 class="abs hero-title">concept. create. complete.</h1>
</section>

<section class="intro">
  <h2 class="abs headline design-title">Design Happens Here</h2>
  <p class="abs copy design-copy">We are leading the way in design innovation for modern websites. Clean, functional, intuitive websites for progressive businesses.</p>
  <h2 class="abs headline art-title">Art Happens Here</h2>
  <p class="abs copy art-copy">Building brands through design, we believe that contrast is everything. For industry leaders who set the pace and exceed expectations, we help give the company voice and soul.</p>
  <h2 class="abs headline ideas-title">Ideas Happen Here</h2>
  <p class="abs copy ideas-copy">Clients look to us for unique, exceptional solutions to their technology issues. We bring creativity to the table and solve your business' problems with actionable solutions.</p>
</section>

<section class="team">
  <h2 class="abs headline team-title">The Cedar Team</h2>
  <p class="abs team-copy"><strong>Cedar Lane Studio</strong> focuses on creating extraordinary online experiences for extraordinary clients. We'll work with you to create the perfect online presence for your brand.</p>
  <h2 class="abs headline size-title">Size is Everything</h2>
  <p class="abs size-copy"><strong>We don’t work in a massive corporate office and we don’t have a mailroom.</strong> Not that there’s anything wrong with that, it’s just that we like knowing each other’s names, and encourage our clients to know ours. Our small staff has an advantage – our group works more efficiently, more cost-effectively and most importantly, flexible to each client’s unique needs. We deliver a range of services found at any agency, with the personal service you deserve.</p>
</section>

<section class="goal">
  <h2 class="abs headline goal-title">Our Goal</h2>
  <p class="abs copy goal-copy"><strong>Cedar Lane Studio brings your brand to life</strong>, online. We do it all when it comes to online commerce for retail stores, wholesalers and distributors. Taking your company online introduces a world of opportunity, as well as specific challenges associated with online trade. We’ll assist you in establishing a successful online presence and bringing your brand to a worldwide audience.</p>
  <h2 class="abs headline who-title">Who's Miles?</h2>
  <p class="abs copy who-copy"><strong>Miles Harlan, owner of Cedar Lane Studio is not</strong> your typical principal. He’s worked internationally with both Halden Press and Brightwell Media publications in photo production for titles including Metropolitan Weekly and Gilded Hour. Originally from coastal Maine and an all-around New Englander, Miles can often be found sailing during the summer and skiing during winter. He believes that inspiration comes from experiencing the world, not from sitting in a cubicle. But no worries, his biggest fear is being offline, and is always within an arms reach of the Internet.</p>
</section>

<section class="get-you">
  <h2 class="abs headline get-title">We Get You.</h2>
  <div class="abs get-copy">
    <p>Having a website isn’t enough. You need to show your customers you understand the socially connected online world we live in.</p>
    <p>We help you create designs that capture the personality of your business and project the image you want your customers to see. Maybe you’re a small company looking to sell yourself in the big leagues; maybe you’re a big company that wants to look approachable; either way, we can make it happen.</p>
    <p>You’ll come across looking professional, unique and strikingly hip all at the same time.</p>
  </div>
</section>

<section class="contact">
  <p class="abs contact-email">hello@cedarlanestudio.com</p>
  <h3 class="abs form-title">Contact Form</h3>
  <div class="abs field field-name">Name</div>
  <div class="abs field field-email">Email</div>
  <div class="abs field field-phone">Phone</div>
  <div class="abs field field-message">Mesage</div>
  <div class="abs send-btn">Send</div>
</section>

<footer class="site-footer">
  <div class="abs social" aria-label="Social links">
    <span></span><span></span><span></span><span></span><span></span><span></span><span></span>
  </div>
  <span class="abs newsletter-label">JOIN OUR NEWSLETTER</span>
  <div class="abs newsletter-input">Email address</div>
  <div class="abs footer-rule"></div>
  <ul class="abs footer-links">
    <li><a href="#">Home</a></li><li><a href="#">FAQ</a></li><li><a href="#">About us</a></li><li><a href="#">Press kit</a></li>
    <li><a href="#">Services</a></li><li><a href="#">Privacy policy</a></li><li><a href="#">Contact us</a></li><li><a href="#">Investors</a></li>
  </ul>
</footer>

<div class="abs base" style="left:0;width:1200px">
  <span class="abs shop">Shop locator ›</span>
  <span class="abs pay-note">We accept all popular payment methods</span>
  <div class="abs cards" aria-label="Accepted payments">
    <span></span><span></span><span></span><span></span><span></span><span></span><span></span><span></span>
  </div>
  <span class="abs copyright">© 2016 All rights reserved</span>
  <div class="abs base-links"><span>Terms &amp; conditions</span><span>Privacy policy</span></div>
</div>

</body>
</html>
```